Visitenkarten-Design für architect i.a.
Aufgabenstellung
Logo ( Siehe Anhang)
scrinari
dessignader da construcziun aulta
maturitad professiunla
architect i.a.

```html
<!DOCTYPE html>
<html lang="de">
<head>
<meta charset="utf-8">
<title>Vorlin – Visitenkarten</title>
<link rel="stylesheet" href="https://fonts.googleapis.com/css2?family=Quicksand:wght@400;500;600;700&display=swap">
<style>
  :root {
    --stage: #ece9e4;
    --paper: #ffffff;
    --slate: #4b5f6d;
    --teal: #1ea79c;
    --ink: #3d4a54;
    --ink-soft: #6d7880;
    --line: #c9d0d4;
    --sky: #5fa8c9;
  }
  * { box-sizing: border-box; margin: 0; padding: 0; }
  html, body { width: 1200px; height: 892px; overflow: hidden; }
  body {
    background: var(--stage);
    font-family: "Quicksand", sans-serif;
    position: relative;
  }
  .card {
    position: absolute;
    top: 296px;
    width: 520px;
    height: 300px;
    box-shadow: 0 10px 28px rgba(0,0,0,.18);
    overflow: hidden;
  }
  /* front */
  .card--front { left: 50px; background: var(--paper); }
  .brand {
    position: absolute;
    display: flex;
    align-items: center;
    gap: 12px;
  }
  .brand__mark { display: block; }
  .brand__name { font-weight: 700; letter-spacing: 1px; line-height: 1; }
  .brand__tagline { font-weight: 500; line-height: 1; }

  .card--front .brand { top: 34px; right: 40px; }
  .card--front .brand__mark { width: 22px; height: 22px; background: var(--sky); }
  .card--front .brand__name { font-size: 54px; color: var(--ink); }
  .card--front .brand__tagline {
    position: absolute; top: 96px; right: 40px;
    font-size: 19px; color: var(--ink); letter-spacing: .5px;
  }

  .nameband {
    position: absolute; left: 0; right: 0; top: 128px; height: 66px;
    background: var(--teal);
    text-align: right;
    padding: 6px 40px 0 0;
    color: var(--paper);
  }
  .nameband__name { font-size: 30px; font-weight: 500; line-height: 1.05; }
  .nameband__role { font-size: 17px; font-weight: 500; color: #e4f5f3; }

  .address {
    position: absolute; left: 36px; top: 216px;
    font-size: 11px; font-weight: 600; font-style: normal; color: var(--ink-soft);
    text-transform: uppercase; line-height: 1.55; letter-spacing: .3px;
  }
  .divider {
    position: absolute; left: 300px; top: 212px; width: 1px; height: 64px;
    background: var(--line);
  }
  .contact {
    position: absolute; left: 318px; top: 214px;
    display: flex; flex-direction: column; gap: 12px;
  }
  .contact__row {
    display: flex; align-items: center; gap: 8px;
    font-size: 11px; font-weight: 600; color: var(--ink-soft);
  }
  .contact__icon { width: 20px; height: 20px; flex: none; }

  /* back */
  .card--back { left: 630px; background: var(--slate); }
  .card--back .brand { top: 104px; left: 0; right: 0; justify-content: center; }
  .card--back .brand__mark { width: 24px; height: 24px; background: var(--paper); }
  .card--back .brand__name { font-size: 62px; color: var(--paper); }
  .card--back .brand__tagline {
    position: absolute; top: 178px; left: 0; right: 0; text-align: center;
    font-size: 22px; color: var(--paper); letter-spacing: .5px;
  }
</style>
</head>
<body>
  <section class="card card--front" aria-label="Visitenkarte Vorderseite">
    <div class="brand">
      <span class="brand__mark"></span>
      <span class="brand__name">vorlin</span>
    </div>
    <p class="brand__tagline">plans cun precisiun</p>

    <div class="nameband">
      <p class="nameband__name">Lorin T. Asketta</p>
      <p class="nameband__role">consultant</p>
    </div>

    <address class="address">
      Vorlin urban accommodation<br>
      Tannenweg 17 ateliers<br>
      6020 Sorwil
    </address>
    <span class="divider"></span>

    <div class="contact">
      <p class="contact__row">
        <svg class="contact__icon" viewBox="0 0 20 20" aria-hidden="true">
          <circle cx="10" cy="10" r="10" fill="var(--sky)"/>
          <path d="M7 5.5l2 2-1 1.3c.7 1.5 1.7 2.5 3.2 3.2l1.3-1 2 2-1.2 1.5c-3.4-.4-6.9-3.9-7.3-7.3z" fill="#fff"/>
        </svg>
        NAT. 079 410 27 63
      </p>
      <p class="contact__row">
        <svg class="contact__icon" viewBox="0 0 20 20" aria-hidden="true">
          <circle cx="10" cy="10" r="10" fill="var(--ink-soft)"/>
          <rect x="5" y="6.5" width="10" height="7" rx="1" fill="#fff"/>
          <path d="M5.5 7l4.5 3.5L14.5 7" fill="none" stroke="var(--ink-soft)" stroke-width="1"/>
        </svg>
        info@vorlinkasper.ch
      </p>
    </div>
  </section>

  <section class="card card--back" aria-label="Visitenkarte Rückseite">
    <div class="brand">
      <span class="brand__mark"></span>
      <span class="brand__name">vorlin</span>
    </div>
    <p class="brand__tagline">plans cun precisiun</p>
  </section>
</body>
</html>
```